依頼詳細
【デザイン改善要望】

・Klipora上のサムネイルのクリック率を上げたいで、インパクトのあるデザインをお願いします。

・Kliporaのサムネイルはやはり人(演者)の写真が入ったほうがインパクトが高いですが、このチャンネルはパペット人形をキャラクターにしているため、人に比べてインパクトが劣ります。そこをデザインの力でインパクトを出したいです。

・キャラクターは「写真」と「イラスト」のどちらも素材として添付しますので、デザインによって、どちらをお使い頂いても構いません。

・サムネイルでチャンネルの世界観を作りたいので、複数枚並んだ時に、全体として統一感が必要です。

【今後の継続依頼】

・今回のコンペで当選した場合、当選者の方にすべてのサムネイルの制作をお願いしたく思っております。

・当選後に別依頼として、50枚25,000円(コモリー受取額・税別)の金額条件にはお受け頂ける方を希望します。

・継続依頼を受けることができない、または、上記の条件では継続依頼を受けることができない方は、コンペへのご応募をお控え頂けますよう、お願い致します。
記載項目
動画キャッチコピー+キャラクター
サイズ
• 「横1280×縦720」×3つ
希望イメージ
シンプル 複雑
単色 カラフル
暗い 明るい
日常 高級
遊び心 厳粛
未来的 伝統的
女性的 男性的
希望する色
納品ファイル
• 高解像度JPG (.jpg)
• イラストレーター形式 (.ai)
• フォトショップ形式 (.psd)
• PNG形式 (.png)
補足説明
■ 選んだ理由

最もイメージに近いデザインをご提案頂き、誠にありがとうございました。また修正にも快く対応頂き、感謝しております。

■ 提案者全員のお礼・コメント

この度は当コンペにご参加頂き、誠にありがとうございました。たくさんの応募を頂き、どれも素晴らしいご提案で、とても選定が難しかったです。またの機会にぜひ宜しくお願い致します。

```html
<!DOCTYPE html>
<html lang="ja">
<head>
<meta charset="utf-8">
<title>サムネイル 3点セット</title>
<link rel="stylesheet" href="https://fonts.googleapis.com/css2?family=M+PLUS+Rounded+1c:wght@800;900&display=swap">
<style>
  :root {
    --ink: #111111;
    --red: #e60012;
    --deep-red: #9e000b;
    --yellow: #ffe600;
    --sun-core: #fffbe0;
    --sun-mid: #ffe94d;
    --sun-edge: #ff9a1a;
    --pastel-edge: #ff9fba;
    --white: #ffffff;
    --monkey: #8a4a22;
    --zebra: #f2e6cf;
  }
  * { box-sizing: border-box; margin: 0; padding: 0; }
  html, body { width: 717px; height: 1200px; overflow: hidden; background: var(--white); }
  body { font-family: "M PLUS Rounded 1c", sans-serif; font-weight: 900; position: relative; }

  .thumb { position: absolute; left: 0; width: 717px; height: 385px; overflow: hidden; }
  .thumb--intro { top: 0; background: radial-gradient(ellipse at 50% 55%, var(--sun-core) 0%, var(--sun-mid) 45%, var(--sun-edge) 100%); }
  .thumb--listen { top: 405px; background: radial-gradient(ellipse at 50% 55%, var(--sun-core) 0%, var(--sun-mid) 45%, var(--sun-edge) 100%); }
  .thumb--chara { top: 815px; background: radial-gradient(ellipse at 50% 55%, var(--sun-core) 0%, #fff27a 40%, var(--pastel-edge) 100%); }

  .character { position: absolute; border-radius: 45% 45% 40% 40%; }
  .character--monkey { background: radial-gradient(circle at 50% 40%, #b36a38, var(--monkey)); }
  .character--zebra { background: radial-gradient(circle at 50% 40%, #fffaf0, var(--zebra)); border: 4px solid #5a3a20; }

  .copy { position: absolute; left: 0; top: 0; width: 717px; height: 385px; }
  .copy text { font-family: "M PLUS Rounded 1c", sans-serif; font-weight: 900; text-anchor: middle; paint-order: stroke fill; stroke-linejoin: round; }
  .t-ink { fill: var(--ink); stroke: var(--white); stroke-width: 10px; }
  .t-red { fill: var(--red); stroke: var(--white); stroke-width: 10px; }
  .t-plain { fill: var(--ink); stroke: none; }
  .t-white { fill: var(--white); stroke: none; }
  .t-yellow { fill: var(--yellow); stroke: var(--deep-red); stroke-width: 10px; }
  .t-outer { fill: var(--red); stroke: var(--deep-red); stroke-width: 26px; }
  .t-inner { fill: var(--red); stroke: var(--white); stroke-width: 14px; }
  .badge { fill: var(--yellow); }
  .label-box { fill: var(--red); stroke: var(--white); stroke-width: 5px; }
</style>
</head>
<body>

<section class="thumb thumb--intro">
  <div class="character character--monkey" role="img" aria-label="サルのパペットキャラクター" style="left:30px; top:90px; width:170px; height:240px;"></div>
  <div class="character character--zebra" role="img" aria-label="シマウマのパペットキャラクター" style="left:505px; top:95px; width:190px; height:240px;"></div>
  <svg class="copy" viewBox="0 0 717 385">
    <rect class="badge" x="228" y="6" width="261" height="46" rx="23"/>
    <text class="t-plain" x="358" y="42" font-size="32">たった<tspan fill="#e60012" font-size="40">1</tspan>分で</text>
    <text class="t-ink" x="358" y="110" font-size="56">仕事も人生も変える</text>
    <text class="t-red" x="358" y="150" font-size="30">新しい</text>
    <rect class="label-box" x="190" y="158" width="337" height="88" rx="10"/>
    <text class="t-white" x="358" y="228" font-size="74">自己紹介</text>
    <text class="t-red" x="358" y="290" font-size="38">の仕方</text>
  </svg>
</section>

<section class="thumb thumb--listen">
  <div class="character character--monkey" role="img" aria-label="サルのパペットキャラクター" style="left:10px; top:80px; width:200px; height:300px;"></div>
  <div class="character character--zebra" role="img" aria-label="シマウマのパペットキャラクター" style="left:525px; top:130px; width:190px; height:250px;"></div>
  <svg class="copy" viewBox="0 0 717 385">
    <text class="t-ink" x="358" y="84" font-size="54">これで会話が上手くいく</text>
    <text class="t-red" x="358" y="205" font-size="104" style="stroke-width:12px">聞き上手</text>
    <text class="t-yellow" x="358" y="298" font-size="58"><tspan fill="#e60012" stroke="#ffffff" font-size="74">3</tspan>つのテクニック</text>
  </svg>
</section>

<section class="thumb thumb--chara">
  <div class="character character--monkey" role="img" aria-label="サルのパペットキャラクター" style="left:20px; top:115px; width:200px; height:270px;"></div>
  <div class="character character--zebra" role="img" aria-label="シマウマのパペットキャラクター" style="left:520px; top:115px; width:190px; height:270px;"></div>
  <svg class="copy" viewBox="0 0 717 385">
    <text class="t-ink" x="358" y="88" font-size="64">仕事がうまくいく</text>
    <text class="t-outer" x="358" y="262" font-size="150">キャラ</text>
    <text class="t-inner" x="358" y="262" font-size="150">キャラ</text>
    <text class="t-ink" x="358" y="345" font-size="42">の作り方</text>
  </svg>
</section>

</body>
</html>
```